New homepage concept needed for online reading programs website

About the Academy of Literacy Growth:
The Institute teaches online summer Bookbright Skills programs for entering fourth graders, offered through partnerships with universities, colleges, and municipalities nationwide. The goal of the program is to build Bookbright Skills (long-word decoding, fluency and comprehension), and foster a lifelong love of books and reading.

Aims & Target Market:
The Institute has developed a new format of its online reading program for fourth graders, which includes live small-group video classes taught by a professional reading teacher. The Institute seeks a mock-up of a homepage of the website used to market this new program. The primary audience for this website is the parents of these 4th graders. Traffic to this website is driven by direct-marketing campaigns directed at parents and students.

Live classes for children are completely new in online education, unlike anything else in the marketplace, and parents therefor have no experience with them. The successful homepage mock-up will include illustrations or photographs that allow visitors to immediately grasp/understand the new format, without relying on a written description. Additionally, the successful homepage concept will make the program, and the video classes in particular, feel fun and appealing to kids and parents alike.

There are three main elements to the program, and each needs to be represented graphically on the homepage, with particular emphasis on the small-group video classes:
1. Live small-group video classes (weekly for six weeks):
a. During video class discussions, the student’s computer (or tablet) screen is filled with live video frames of the teacher and the other students. The video frame for the teacher is larger, and the other students appear in smaller frames.
b. During other video class instruction, the teacher uses a presentation screen to display pages of a book or a “whiteboard” used for instructional activities.
c. The homepage mock-up could include a screenshot of the video classes themselves, with children looking engaged and a teacher leading them in discussion. We have included a screen shot of one of these classes for reference, but do not feel constrained to represent this screen realistically (as shown here). It can be changed around – teacher in the center, etc.). Alternately, if there is a graphic other than a screen shot that you feel could be used to bring across the concept of the video classes, feel free.
2. Individualized online instruction
a. Graphics could include screenshots of the video lessons students complete in between these weekly classes and/or images of a child or children at computer(s).
3. Independent reading in great books
a. Graphics could include some or all of the program books, which can be pulled from our current website (link below), and/or images of a child or children reading.

An example of our current online program website can be seen at http://kestrel.webliteracycourses.example/4/Home. Please reference this site for information on program goals, books/materials, and site navigation.
The successful design will be welcoming and inviting, and allow parents and students to immediately grasp what the programs are, with particular emphasis on the live small-group video classes.

Copy and Specifications:
Sample copy has been provided for reference, as well as a screen shot of our sample classes to show what students will see on screen. Also included are stills of our online video lessons to illustrate the online instruction aspect.

```html
<!DOCTYPE html>
<html lang="en">
<head>
<meta charset="utf-8">
<title>Bookbright Skills – Online Program for 4th and 5th Graders</title>
<link rel="stylesheet" href="https://fonts.googleapis.com/css2?family=Open+Sans:wght@400;600;700&display=swap">
<style>
:root{
  --green:#4aa06b;
  --blue:#1a63b0;
  --sky:#7ec8ef;
  --orange:#f6913d;
  --yellow:#fcc419;
  --band:#53a1d6;
  --footer:#444444;
  --ink:#222222;
  --white:#ffffff;
}
*{box-sizing:border-box;margin:0;padding:0}
html,body{width:1004px;height:1200px;overflow:hidden}
body{font-family:"Open Sans",sans-serif;color:var(--ink);background:var(--white);position:relative}
.abs{position:absolute}

.brand{left:48px;top:6px}
.brand-name{font-size:34px;font-weight:700;color:var(--green);letter-spacing:-0.5px;line-height:40px}
.brand-tag{font-size:14.5px;font-weight:700;color:var(--orange);margin-top:4px}
.phone{right:47px;top:4px;font-size:21px;font-weight:700;display:flex;align-items:center;gap:10px}
.grade-select{left:778px;top:42px;width:180px;height:25px;border:1px solid #bbb;border-radius:3px;background:#f3f3f3;font-size:11px;color:#666;padding:0 8px;display:flex;align-items:center;justify-content:space-between}

.main-nav{left:38px;top:84px;width:928px;height:42px;display:flex}
.main-nav a{color:var(--white);text-decoration:none;font-size:13px;line-height:16px;display:flex;align-items:center;justify-content:center;text-align:center}
.nav-home{width:108px;background:var(--green)}
.nav-indep{width:127px;background:var(--blue)}
.nav-comp{width:128px;background:var(--sky)}
.nav-long{width:119px;background:var(--blue)}
.nav-flu{width:127px;background:var(--orange)}
.nav-about{width:120px;background:var(--yellow)}
.nav-faq{width:103px;background:var(--green)}
.nav-enroll{width:96px;background:var(--blue)}

.hero{left:0;top:126px;width:1004px;height:361px;background:linear-gradient(90deg,#5d4335 0%,#6e4f3b 45%,#7d5a40 70%,#8a6346 100%)}
.hero-title{left:44px;top:54px;width:500px;font-size:16px;font-weight:600;line-height:30px;color:var(--white)}
.benefits{left:56px;top:128px;list-style:none}
.benefits li{display:flex;align-items:center;gap:17px;height:30.2px;font-size:14px;color:var(--white)}
.hero-btn{left:48px;top:273px;width:140px;height:39px;background:var(--yellow);color:var(--ink);font-size:17px;font-weight:600;display:flex;align-items:center;justify-content:center;border-radius:2px;box-shadow:2px 3px 4px rgba(0,0,0,.35)}
.video-frame{left:545px;top:63px;width:397px;height:235px;background:#6a584c;border-radius:6px;padding:7px}
.video-still{width:100%;height:100%;background:linear-gradient(90deg,#4f9ad8,#3f8ed6);position:relative}
.video-still svg{position:absolute;left:145px;top:65px}
.slider-dots{left:479px;top:335px;display:flex;gap:5px}
.slider-dots span{width:12px;height:12px;border-radius:50%;background:var(--green)}
.slider-dots .on{background:var(--yellow)}

.feature{top:520px;width:292px;height:372px;border-radius:3px;overflow:hidden;color:var(--white);text-align:center}
.feature h2{height:36px;font-size:16px;font-weight:600;line-height:36px}
.feature-photo{height:189px;margin:0 1px}
.feature p{font-size:13px;line-height:21px;padding:10px 16px 0}
.feature .more{position:absolute;left:50%;transform:translateX(-50%);top:329px;background:var(--white);font-size:16px;font-weight:600;padding:0 10px;height:34px;line-height:34px;border-radius:2px}
.f-live{left:38px;background:var(--green)}
.f-live .more{color:var(--green)}
.f-live .feature-photo{background:linear-gradient(135deg,#d8c8b8,#b9a28f 60%,#c6b8a8)}
.f-indiv{left:356px;background:var(--blue)}
.f-indiv .more{color:var(--blue)}
.f-indiv .feature-photo{background:linear-gradient(135deg,#eef0ec,#c8b3a2 55%,#e6e4df)}
.f-books{left:674px;background:var(--orange)}
.f-books .more{color:var(--orange)}
.f-books .feature-photo{background:linear-gradient(135deg,#b9a48a,#d9cdbd 55%,#c3aa92)}

.action-band{left:0;top:927px;width:1004px;height:131px;background:var(--band)}
.action{top:32px;width:241px;height:69px;background:var(--white);display:flex;align-items:center;gap:9px;padding-left:11px;font-size:16px;font-weight:600;line-height:25px;color:var(--ink)}

.site-footer{left:0;top:1058px;width:1004px;height:142px;background:var(--footer)}
.social{top:26px;width:42px;height:42px;border:2px solid var(--white);border-radius:3px}
.copyright{left:0;top:86px;width:1004px;text-align:center;font-size:13px;color:var(--white)}
.copyright a{color:var(--yellow);text-decoration:none}
</style>
</head>
<body>

<header>
  <div class="abs brand">
    <div class="brand-name">Bookbright Skills</div>
    <div class="brand-tag">Online Program for 4th and 5th Graders</div>
  </div>
  <div class="abs phone">
    <svg width="18" height="18" viewBox="0 0 24 24"><path fill="#222" d="M6.6 10.8a15.1 15.1 0 0 0 6.6 6.6l2.2-2.2a1 1 0 0 1 1-.25 11.4 11.4 0 0 0 3.6.57 1 1 0 0 1 1 1V20a1 1 0 0 1-1 1A17 17 0 0 1 3 4a1 1 0 0 1 1-1h3.5a1 1 0 0 1 1 1c0 1.25.2 2.45.57 3.57a1 1 0 0 1-.25 1z"/></svg>
    1-800-555-0142
  </div>
  <div class="abs grade-select">4th-5th Graders
    <svg width="10" height="6" viewBox="0 0 10 6"><path d="M1 1l4 4 4-4" stroke="#333" stroke-width="1.6" fill="none"/></svg>
  </div>
  <nav class="abs main-nav">
    <a class="nav-home">Home</a>
    <a class="nav-indep">Independent<br>Reading</a>
    <a class="nav-comp">Comprehension</a>
    <a class="nav-long">Long-Word<br>Decoding</a>
    <a class="nav-flu">Fluency &amp; Speed</a>
    <a class="nav-about">About the<br>Teachers</a>
    <a class="nav-faq">FAQ</a>
    <a class="nav-enroll">Enroll</a>
  </nav>
</header>

<section class="abs hero" role="img" aria-label="Photo of smiling children reading together">
  <p class="abs hero-title">This program will help your child become a skilled, enthusiastic reader with strong comprehension. Your child will:</p>
  <ul class="abs benefits">
    <li><svg width="17" height="14" viewBox="0 0 17 14"><path d="M1.5 7.5l4.5 4.5L15.5 1.5" stroke="#fff" stroke-width="3" fill="none"/></svg>Build long-word decoding skills</li>
    <li><svg width="17" height="14" viewBox="0 0 17 14"><path d="M1.5 7.5l4.5 4.5L15.5 1.5" stroke="#fff" stroke-width="3" fill="none"/></svg>Read more fluently and rapidly</li>
    <li><svg width="17" height="14" viewBox="0 0 17 14"><path d="M1.5 7.5l4.5 4.5L15.5 1.5" stroke="#fff" stroke-width="3" fill="none"/></svg>Improve comprehension</li>
    <li><svg width="17" height="14" viewBox="0 0 17 14"><path d="M1.5 7.5l4.5 4.5L15.5 1.5" stroke="#fff" stroke-width="3" fill="none"/></svg>Become a strong, enthusiastic reader</li>
  </ul>
  <div class="abs hero-btn">Learn More</div>
  <div class="abs video-frame">
    <div class="video-still" role="img" aria-label="Video still of a teacher holding a book beside a program lesson page">
      <svg width="94" height="94" viewBox="0 0 94 94"><circle cx="47" cy="47" r="44" stroke="rgba(255,255,255,.7)" stroke-width="5" fill="none"/><path d="M37 28l28 19-28 19z" fill="rgba(255,255,255,.7)"/></svg>
    </div>
  </div>
  <div class="abs slider-dots"><span></span><span class="on"></span><span></span></div>
</section>

<section>
  <article class="abs feature f-live">
    <h2>Live Small-Group Video Classes</h2>
    <div class="feature-photo" role="img" aria-label="Photo of three children gathered around a tablet"></div>
    <p>Lorem Ipsum is simply dummy text of the printing and typesetting industry. Lorem Ipsum has been the industry's standard dummy text ever since the 1500s</p>
    <span class="more">Learn More</span>
  </article>
  <article class="abs feature f-indiv">
    <h2>Individualized Online Instruction</h2>
    <div class="feature-photo" role="img" aria-label="Photo of a parent helping a child with a lesson"></div>
    <p>Lorem Ipsum is simply dummy text of the printing and typesetting industry. Lorem Ipsum has been the industry's standard dummy text ever since the 1500s</p>
    <span class="more">Learn More</span>
  </article>
  <article class="abs feature f-books">
    <h2>Independent Reading In Great Books</h2>
    <div class="feature-photo" role="img" aria-label="Photo of a girl reading on a tablet at a desk"></div>
    <p>Lorem Ipsum is simply dummy text of the printing and typesetting industry. Lorem Ipsum has been the industry's standard dummy text ever since the 1500s</p>
    <span class="more">Learn More</span>
  </article>
</section>

<section class="abs action-band">
  <div class="abs action" style="left:60px">
    <svg width="34" height="34" viewBox="0 0 34 34"><rect x="3" y="5" width="22" height="27" rx="2" stroke="#222" stroke-width="2.2" fill="none"/><path d="M7 12h12M7 17h10M7 22h8" stroke="#222" stroke-width="2"/><path d="M29 8l3 3-13 13-4 1 1-4z" fill="#222"/><path d="M8 2v5M14 2v5M20 2v5" stroke="#222" stroke-width="2"/></svg>
    Registration Information
  </div>
  <div class="abs action" style="left:379px">
    <svg width="38" height="40" viewBox="0 0 38 40"><rect x="14" y="2" width="16" height="28" rx="3" fill="#222"/><rect x="17" y="6" width="10" height="18" fill="#fff"/><path d="M3 36c0-8 4-14 12-16l3 6c-4 1-6 4-7 10z" fill="#222"/><path d="M32 8l4-2M32 14h5M32 20l4 2" stroke="#222" stroke-width="2"/></svg>
    <span>Enroll By Phone<br>1-800-555-0142</span>
  </div>
  <div class="abs action" style="left:698px">
    <svg width="36" height="34" viewBox="0 0 36 34"><rect x="3" y="2" width="22" height="28" rx="2" stroke="#222" stroke-width="2.4" fill="none"/><path d="M7 9h14M7 14h14M7 19h9" stroke="#222" stroke-width="2.2"/><path d="M17 24l5 5 11-12" stroke="#222" stroke-width="3.2" fill="none"/></svg>
    Enroll Online Now
  </div>
</section>

<footer class="abs site-footer">
  <span class="abs social" style="left:364px" aria-label="Social link"></span>
  <span class="abs social" style="left:422px" aria-label="Social link"></span>
  <span class="abs social" style="left:481px" aria-label="Social link"></span>
  <span class="abs social" style="left:540px" aria-label="Social link"></span>
  <span class="abs social" style="left:598px" aria-label="Social link"></span>
  <p class="abs copyright">Copyright © 2014 Academy of Literacy Growth I <a>Privacy Policy</a></p>
</footer>

</body>
</html>
```